Steady Harbor Stewardship Graphics

We need help to design a logo, graphics, layout that will represent a particular type of leadership consulting business that we are about to launch. The design/graphics should be able to be used for developing a brochure, web page, advertisements, letterhead, business cards, etc. The leadership consulting business that we are launching is called “Steady Harbor Stewardship.” We would like to start with the design of a brochure. We have enclosed a draft to give you some ideas about the type of graphics we are looking for. The graphics should include fonts, colors, pictures/symbols, and layout initially for the brochure only. There are three draft pictures/symbols that we have gotten from the internet for the attached brochure that may be copyrighted. We would like you to develop something similar, but original for each of the graphic’s. They each represent a theme/topic that we will be using. For example, the graphic for the section titled “What is Steady Harbor Stewardship?” has a picture/graphic that has a diverse group of people to represent the idea of Collective Leadership. It leaves out some of the facial features for each person in order to make sure that there are no similarities to real persons. We need something similar to this. The graphic for “Why is Steady Harbor Stewardship important?”, uses a picture of “ice” and a “mouse.” “Mice and Ice” is a key metaphor that we will use in our business. We need something to represent this concept. The same is true for the third picture that represents ripples in water. After design of the brochure we may seek additional help for the web page and other items.

Target Market(s)

Government and business organizations

Colors

Designer to choose colors to be used in the design.

Requirements
Must have
• Brochure Design
Nice to have
• Logos

```html
<!DOCTYPE html>
<html lang="en">
<head>
<meta charset="utf-8">
<title>Steady Harbor Stewardship – Brochure Cover</title>
<link href="https://fonts.googleapis.com/css2?family=Cookie&family=Roboto+Slab:wght@400;700&display=swap" rel="stylesheet">
<style>
  :root {
    --panel-grey: #e1e1e1;
    --navy: #121d62;
    --navy-light: #1d2c7c;
    --white: #ffffff;
    --ink: #ffffff;
  }
  html, body {
    margin: 0;
    padding: 0;
    width: 1153px;
    height: 1200px;
    overflow: hidden;
    background: var(--white);
  }
  .spread {
    position: relative;
    width: 1153px;
    height: 1200px;
  }
  .inner-panel {
    position: absolute;
    left: 0;
    top: 0;
    width: 637px;
    height: 1200px;
    background: var(--panel-grey);
  }
  .cover-panel {
    position: absolute;
    left: 637px;
    top: 0;
    width: 516px;
    height: 1200px;
    background: var(--white);
    overflow: hidden;
  }
  .cover-field {
    position: absolute;
    left: 0;
    top: 282px;
    width: 516px;
    height: 918px;
    background: radial-gradient(circle at 50% 10%, var(--navy-light) 0%, var(--navy) 75%);
  }
  .name-cutout {
    position: absolute;
    left: 64px;
    top: 95px;
    width: 392px;
    height: 392px;
    border-radius: 50%;
    background: var(--white);
  }
  .brand-mark {
    position: absolute;
    left: 64px;
    top: 95px;
    width: 392px;
    height: 392px;
    display: flex;
    flex-direction: column;
    align-items: center;
    justify-content: center;
    gap: 14px;
  }
  .brand-dot {
    width: 28px;
    height: 28px;
    border-radius: 50%;
    background: var(--navy);
  }
  .brand-name {
    margin: 0;
    font-family: "Roboto Slab", "Rockwell", Georgia, serif;
    font-weight: 700;
    font-size: 32px;
    line-height: 1.2;
    letter-spacing: 1px;
    text-transform: uppercase;
    text-align: center;
    color: var(--navy);
  }
  .tagline {
    position: absolute;
    left: 0;
    top: 618px;
    width: 516px;
    margin: 0;
    font-family: "Cookie", cursive;
    font-size: 34px;
    line-height: 40px;
    text-align: center;
    color: var(--ink);
  }
  .authors {
    position: absolute;
    left: 0;
    top: 1012px;
    width: 516px;
    margin: 0;
    font-family: "Roboto Slab", "Rockwell", Georgia, serif;
    font-weight: 400;
    font-size: 22px;
    line-height: 28px;
    text-align: center;
    color: var(--ink);
  }
</style>
</head>
<body>
  <main class="spread">
    <section class="inner-panel" aria-label="Inside flap"></section>
    <section class="cover-panel">
      <div class="cover-field" role="img" aria-label="Navy background with soft radiating sunburst rays"></div>
      <div class="name-cutout"></div>
      <div class="brand-mark">
        <span class="brand-dot"></span>
        <h1 class="brand-name">Steady Harbor<br>Stewardship</h1>
      </div>
      <p class="tagline">Discover and Unite<br>the Shared Stewardship<br>Across Your Whole Team</p>
      <p class="authors">Dale Hartwell and<br>Nora Castell</p>
    </section>
  </main>
</body>
</html>
```